Einladungskarten für 30-jähriges Jubiläum
Zielgruppe
Wir sind ein Kompetenzzentrum für Gesundheit, Fitness und Regulationsmedizin. Im April 2024 feiern wir 30-jähriges Jubiläum. Wir haben in den Jahrzehnten viele Gesundheitsbewusste, Führungskräfte, Manager und Sportler betreut und uns als Mikronährstoffanalyse experten etabliert. Der Slogen 'Kraft nach Plan' resuliert aus den Ergebnissen der speziellen Blutanalysen, die als Ergebnis Empfehlungen für Supplemente haben, zusammengestellt wie ein Kochrezept, deshalb 'Kraft nach Plan'.
Aufgabenstellung
Eine seriöse SAFE THE DATE Karte (Formal ist egal) und daraus resultierend die Einladungskarte. Die Karten sollen per Post verschickt werden. Unsere Firmenfarben sind grün und blau. DIN-A-5 als Klappkarte für die Einladung wäre wünschenswert, da wir den Programmablauf mit aufnehmen möchten.

```html
<!DOCTYPE html>
<html lang="de">
<head>
<meta charset="utf-8">
<title>Einladung – 30 Jahre VITARO</title>
<link rel="stylesheet" href="https://fonts.googleapis.com/css2?family=Archivo+Black&family=Jost:wght@300;400;500;600&display=swap">
<style>
  :root {
    --bg: #dedede;
    --green: #72b35a;
    --green-light: #94c97f;
    --green-soft: #cfe5c5;
    --blue: #6f8ccc;
    --blue-dark: #3f5fa8;
    --paper: #f4f4f4;
    --paper-shade: #ebebeb;
    --white: #ffffff;
    --font-head: "Archivo Black", "Arial Black", sans-serif;
    --font-body: "Jost", "Futura", sans-serif;
  }
  * { box-sizing: border-box; margin: 0; padding: 0; }
  html, body { width: 1200px; height: 769px; overflow: hidden; background: var(--bg); }
  .canvas { position: relative; width: 1200px; height: 769px; }

  .spread { position: absolute; left: 40px; width: 1120px; height: 345px; display: flex; box-shadow: 0 6px 18px rgba(0,0,0,.12); }
  .spread--outside { top: 25px; }
  .spread--inside { top: 399px; }
  .panel { position: relative; width: 560px; height: 100%; }

  .panel--back { background: var(--green); display: flex; flex-direction: column; align-items: center; justify-content: center; }
  .panel--cover { background: var(--green-light); border-left: 1px solid rgba(0,0,0,.08); display: flex; flex-direction: column; align-items: center; justify-content: center; }
  .panel--greeting { background: var(--paper); text-align: center; overflow: hidden; }
  .panel--program { background: var(--paper-shade); border-left: 1px solid rgba(0,0,0,.06); padding: 42px 46px 30px 52px; }

  .back-greeting { font-family: var(--font-body); font-weight: 300; color: var(--white); font-size: 22px; margin-bottom: 18px; }

  .brand { font-family: var(--font-body); font-weight: 600; color: var(--white); font-size: 28px; letter-spacing: 2px; line-height: 1; }
  .brand--small { font-size: 20px; }

  .event-title { font-family: var(--font-body); font-weight: 600; color: var(--white); font-size: 48px; line-height: 1; text-align: center; }
  .event-subtitle { font-family: var(--font-body); font-weight: 500; color: var(--blue-dark); font-size: 18px; margin: 12px 0 48px; }

  .confetti { position: absolute; left: 40px; right: 40px; top: 18px; height: 36px; background: linear-gradient(90deg, rgba(114,179,90,.08), rgba(114,179,90,.22), rgba(114,179,90,.08)); border-radius: 6px; }
  .jubilee { position: absolute; left: 0; right: 0; top: 72px; }
  .jubilee__title { font-family: var(--font-head); color: var(--green); text-transform: uppercase; line-height: .95; }
  .jubilee__title span { display: block; }
  .jubilee__title .line-1 { font-size: 30px; }
  .jubilee__title .line-2 { font-size: 40px; }
  .jubilee__facts { margin-top: 16px; font-family: var(--font-body); font-weight: 300; color: var(--blue-dark); font-size: 15.5px; line-height: 1.45; }
  .jubilee__facts b { font-weight: 600; }
  .balloons { position: absolute; left: 90px; right: 90px; bottom: 0; height: 92px; background: linear-gradient(180deg, rgba(114,179,90,.30), rgba(114,179,90,.10)); border-radius: 30px 30px 0 0; }

  .program__title { font-family: var(--font-head); color: var(--green); font-size: 22px; letter-spacing: .5px; line-height: 1; }
  .program__lead { font-family: var(--font-body); color: var(--blue-dark); font-size: 14px; margin: 4px 0 16px; }
  .program__item { margin-bottom: 14px; }
  .program__heading { font-family: var(--font-head); color: var(--blue-dark); font-size: 12px; text-transform: uppercase; letter-spacing: .4px; }
  .program__text { font-family: var(--font-body); color: var(--blue-dark); font-size: 12.5px; line-height: 1.4; font-weight: 400; }
</style>
</head>
<body>
<main class="canvas">

  <section class="spread spread--outside" aria-label="Außenseite der Klappkarte">
    <article class="panel panel--back">
      <p class="back-greeting">Wir freuen uns auf Euch!</p>
      <p class="brand">VITARO</p>
    </article>
    <article class="panel panel--cover">
      <h1 class="event-title">Kraft nach Plan</h1>
      <p class="event-subtitle">Wirtschafts- &amp; Gesundheitsforum</p>
      <p class="brand brand--small">VITARO</p>
    </article>
  </section>

  <section class="spread spread--inside" aria-label="Innenseite der Klappkarte">
    <article class="panel panel--greeting">
      <div class="confetti" role="img" aria-label="Grünes Konfetti als Dekoration"></div>
      <div class="jubilee">
        <h2 class="jubilee__title"><span class="line-1">Wir werden</span><span class="line-2">30 Jahre</span></h2>
        <p class="jubilee__facts">
          <b>Wann?</b> Donnerstag, 18. April 2024 um 19.00 Uhr<br>
          <b>Wo?</b> Sieger Lounge, Lindenhof Arena in Lindental
        </p>
      </div>
      <div class="balloons" role="img" aria-label="Fünf grüne Luftballons als Linienzeichnung"></div>
    </article>
    <article class="panel panel--program">
      <h2 class="program__title">PROGRAMM</h2>
      <p class="program__lead">Wirtschafts- und Gesundheitsforum „Kraft nach Plan“</p>
      <div class="program__item">
        <h3 class="program__heading">Überschrift 1</h3>
        <p class="program__text">Begrüßung der Gäste durch die Geschäftsführung mit einem Rückblick auf drei Jahrzehnte Arbeit für Gesundheit, Fitness und Leistung im Alltag.</p>
      </div>
      <div class="program__item">
        <h3 class="program__heading">Überschrift 2</h3>
        <p class="program__text">Impulsvortrag zur Blutanalyse und wie aus den Werten ein persönlicher Plan für mehr Kraft entsteht, mit Zeit für Fragen der Gäste.</p>
      </div>
      <div class="program__item">
        <h3 class="program__heading">Überschrift 3</h3>
        <p class="program__text">Gemeinsamer Ausklang mit gesundem Buffet, Getränken und guten Gesprächen unter Partnern, Kunden und Freunden bis in den späten Abend hinein.</p>
      </div>
    </article>
  </section>

</main>
</body>
</html>
```